International Fundraising Consultancy needs a new PowerPoint Design

We train international nonprofits on how to fundraise globally. We plan to keep our current logo design and color, as we love the color orange, but want a cleaner, fresher, less cluttered template for our PowerPoint presentations. The finished product needs to be easy to edit, and include template slides that can feature tables, graphics and images. We would like a color scheme for graphics.The layout should be lighter, clear, attractive and easy to read and understand. We also want to use the same template for webinar slides. We have attached an example of our current PowerPoint template with identifying client information removed. The green slide that looks like a clapperboard fro a film is basically just a placeholder that indicates a break for an interactive exercise.

Target Market(s)

Board members, staff members, museum executives, leadership of NGOs, top businesspeople in Europe, many with a modern sense of aesthetics in the art world

Industry/Entity Type

Cleaner

Font styles to use
Sans Serif

Colors
f78f20
f37022

Requirements
Must have
• Orange colors, keep our Vormelinck logo
• Good templates for tables, photos and graphics

```html
<!DOCTYPE html>
<html lang="en">
<head>
<meta charset="utf-8">
<title>Contact Info</title>
<link href="https://fonts.googleapis.com/css2?family=Fira+Sans+Extra+Condensed:wght@600&family=Open+Sans:ital,wght@0,400;0,600;0,700;1,400&display=swap" rel="stylesheet">
<style>
  :root {
    --orange: #f78f20;
    --orange-deep: #f37022;
    --ink: #333333;
    --ink-dark: #1f1f1f;
    --cream: #fbf8f1;
    --cream-edge: #f1ece0;
    --map-sea: #a9c8ec;
    --map-land: #e9ecd9;
  }
  * { margin: 0; padding: 0; box-sizing: border-box; }
  html, body { width: 1200px; height: 900px; overflow: hidden; }
  body { font-family: "Open Sans", Arial, sans-serif; color: var(--ink); }

  .slide {
    position: relative;
    width: 1200px; height: 900px;
    background: radial-gradient(ellipse at 55% 40%, #fffdf8 0%, var(--cream) 55%, var(--cream-edge) 100%);
    overflow: hidden;
  }

  .title-tab {
    position: absolute; left: 0; top: 26px;
    width: 48px; height: 62px;
  }
  .slide-title {
    position: absolute; left: 58px; top: 24px;
    font-family: "Fira Sans Extra Condensed", "Arial Narrow", sans-serif;
    font-weight: 600; font-size: 48px; line-height: 64px;
    color: var(--orange-deep);
  }

  .map-frame {
    position: absolute; left: 70px; top: 170px;
    width: 516px; height: 520px;
    background: #fff; padding: 10px;
    box-shadow: 0 1px 4px rgba(0,0,0,0.25);
  }
  .map-area {
    width: 100%; height: 100%;
    background:
      radial-gradient(ellipse at 62% 70%, var(--map-sea) 0%, var(--map-sea) 28%, transparent 48%),
      linear-gradient(160deg, var(--map-land) 0%, #eef0df 55%, #dfe6cf 100%);
  }

  .contact {
    position: absolute; left: 618px; top: 170px; width: 560px;
  }
  .contact-name {
    font-size: 26px; font-weight: 600; color: var(--orange); line-height: 36px;
  }
  .contact-company { font-size: 20px; line-height: 30px; margin-bottom: 16px; }
  .field-label {
    font-size: 26px; font-weight: 600; color: var(--orange); line-height: 34px;
  }
  .field-value { font-size: 20px; line-height: 25.5px; margin-bottom: 18px; }
  .field-value.address { margin-top: 2px; }

  .social {
    position: absolute; left: 78px; top: 730px;
    display: flex; align-items: center; gap: 18px;
  }
  .social-mark { width: 42px; height: 42px; background: var(--orange-deep); border-radius: 4px; }
  .social-handle {
    font-size: 22px; font-weight: 700; color: var(--ink);
    letter-spacing: 0.3px;
  }

  .brand {
    position: absolute; left: 892px; top: 730px;
    display: flex; align-items: center; gap: 12px;
  }
  .brand-dot { width: 22px; height: 22px; border-radius: 50%; background: var(--orange-deep); }
  .brand-name {
    font-family: "Fira Sans Extra Condensed", "Arial Narrow", sans-serif;
    font-weight: 600; font-size: 30px; color: var(--ink-dark);
  }

  .footer {
    position: absolute; left: 0; top: 808px; width: 1200px; height: 92px;
    border-top: 4px solid #3a3a3a;
    background: linear-gradient(180deg, #fbaa3c 0%, var(--orange) 40%, var(--orange-deep) 100%);
  }
  .slide-number {
    position: absolute; left: 33px; top: 20px;
    width: 57px; height: 54px; border-radius: 6px;
    background: var(--ink-dark); border: 2px solid #555;
    color: #fff; font-size: 27px; line-height: 50px; text-align: center;
  }
  .footer-caption {
    position: absolute; left: 130px; top: 28px;
    font-size: 25px; font-style: italic; color: #fff;
  }
  .nav-button { position: absolute; top: 18px; width: 102px; height: 58px; }
  .nav-button text { font-family: "Open Sans", Arial, sans-serif; font-size: 22px; fill: #fff; }
  .nav-back { left: 957px; }
  .nav-next { left: 1072px; }
</style>
</head>
<body>
<main class="slide">
  <svg class="title-tab" viewBox="0 0 48 62" aria-hidden="true">
    <polygon points="0,0 28,0 48,31 28,62 0,62" fill="#f37022"/>
    <polygon points="0,0 28,0 48,31 0,31" fill="#f78f20"/>
  </svg>
  <h1 class="slide-title">Contact Info</h1>

  <div class="map-frame">
    <div class="map-area" role="img" aria-label="Map of Eastern Europe and the Mediterranean region"></div>
  </div>

  <section class="contact">
    <p class="contact-name">Liesbet Vormelinck, CFRE, Principal</p>
    <p class="contact-company">Vormelinck &amp; Associates</p>

    <p class="field-label">Address</p>
    <p class="field-value address">412 Harbor Road Suite 7,<br>Box 22, Milton,<br>MA 02186 USA</p>

    <p class="field-label">Phone</p>
    <p class="field-value">1(555) 014.2290</p>

    <p class="field-label">FAX</p>
    <p class="field-value">1(555) 014.2290</p>

    <p class="field-label">Email</p>
    <p class="field-value">liesbet@vormelinck.com</p>

    <p class="field-label">Website</p>
    <p class="field-value">www.vormelinck.com</p>
  </section>

  <div class="social">
    <span class="social-mark" aria-hidden="true"></span>
    <span class="social-handle">@VORMELINCK</span>
  </div>

  <div class="brand">
    <span class="brand-dot" aria-hidden="true"></span>
    <span class="brand-name">Vormelinck &amp; Associates</span>
  </div>

  <footer class="footer">
    <div class="slide-number">08</div>
    <p class="footer-caption">Liesbet Vormelinck, CFRE, Principal</p>
    <svg class="nav-button nav-back" viewBox="0 0 102 58" role="button" aria-label="Back">
      <polygon points="16,1 100,1 100,57 16,57 1,29" fill="#1f1f1f" stroke="#555" stroke-width="2"/>
      <text x="58" y="37" text-anchor="middle">Back</text>
    </svg>
    <svg class="nav-button nav-next" viewBox="0 0 102 58" role="button" aria-label="Next">
      <polygon points="2,1 86,1 101,29 86,57 2,57" fill="#1f1f1f" stroke="#555" stroke-width="2"/>
      <text x="44" y="37" text-anchor="middle">Next</text>
    </svg>
  </footer>
</main>
</body>
</html>
```